Fin-Tech Firm Captivating Business Card Design

We need a logo design as well to compliment this business card.

We are a new startup based in Singapore called 'Pardeo Technologies'.

We develop an array of financial solutions ranging from payment convenience to forex trading and remittance.

Our initial product is Mavo - an application which allows user to pre-order food items which would be ready for pickup upon arrival.

We would like to see designs being in black and silver or whatever that looks appealing and exudes a fun and professional feel.

We're not picky as long as it doesn't look like common business cards will do.

I do have a current logo which i do not really like. It will be attached for reference sake

Info:

Pardeo Technologies
Company Registration no. 208716392K

FILE TO BE IN .AI and .PSD

Target Market(s)

-F&B (Online-Ordering)
-Finance(P2P Lending and Forex)

Industry/Entity Type

Finance

Contact Information for Business Card

Name
Position
Contact
Email
Address: 27 Corwen Street, Meridale Tower, #14-05 Singapore 058214

Harlan Webb
Founder, Managing Director
+65 90481736
harlan.w@pardeotech.com

Wei Tan
Founder, Executive Director
+65 93570284
wei.t@pardeotech.com

Logo Text

Pardeo Technologies

Font styles to use
Sans Serif

Requirements
Must have
• Something that has word play about link pard
• Minimalistic but also something that catches The Eye
• Gold/silver on white/black might be nice
• Animal logo ; horse, eagle, bull or bear
Nice to have
• Just make it look fun and cute
• Just a suggestion to make the Y of pardeo stand out
Should not have
• Any landmarks of singapore
• Exclude Pte. Ltd.

```html
<!DOCTYPE html>
<html lang="en">
<head>
<meta charset="utf-8">
<title>Pardeo Technologies – Business Card</title>
<link href="https://fonts.googleapis.com/css2?family=Source+Sans+3:wght@400;600;700&display=swap" rel="stylesheet">
<style>
  :root {
    --backdrop: #2b2b2b;
    --card: #121212;
    --card-edge: #1c1c1c;
    --gold: #f4a81c;
    --silver: #e6e6e6;
    --text: #f2f2f2;
    --muted: #cfcfcf;
    --rule: #3a3a3a;
  }
  * { box-sizing: border-box; margin: 0; padding: 0; }
  html, body {
    width: 1200px; height: 900px; overflow: hidden;
    background: var(--backdrop);
    font-family: "Source Sans 3", sans-serif;
  }
  .stage {
    position: relative; width: 1200px; height: 900px;
    display: flex; align-items: center; justify-content: center; gap: 40px;
  }
  .card {
    position: relative; width: 540px; height: 330px;
    background: var(--card);
    border-radius: 22px;
    box-shadow: 0 0 0 1px var(--card-edge);
  }

  /* Info side */
  .brand-mark {
    position: absolute; left: 60px; top: 95px;
    width: 140px; height: 140px;
    border: 5px solid var(--silver); border-radius: 50%;
    display: flex; align-items: center; justify-content: center;
  }
  .brand-mark__name {
    color: var(--gold); font-weight: 600; font-size: 24px; letter-spacing: 0.5px;
  }
  .divider {
    position: absolute; left: 250px; top: 40px;
    width: 1px; height: 200px; background: var(--rule);
  }
  .details {
    position: absolute; left: 272px; top: 44px; color: var(--text);
  }
  .details__name { color: var(--gold); font-weight: 700; font-size: 21px; line-height: 1.1; }
  .details__role { font-size: 15px; color: var(--muted); margin-top: 2px; }
  .details__address { font-size: 15px; line-height: 1.3; margin-top: 22px; width: 230px; }
  .contact-list { list-style: none; margin-top: 22px; font-size: 15px; }
  .contact-list li { display: flex; align-items: center; gap: 10px; line-height: 1.6; }
  .contact-list svg { width: 12px; height: 12px; flex: none; }
  .icon-fill { fill: var(--gold); }
  .icon-line { fill: none; stroke: var(--card); stroke-width: 2; }
  .registration {
    position: absolute; left: 60px; bottom: 40px;
    font-size: 16px; font-weight: 700; color: var(--gold);
  }
  .registration__number { color: var(--text); }

  /* Brand side */
  .card--brand { display: flex; flex-direction: column; align-items: center; justify-content: center; gap: 18px; }
  .brand-circle {
    width: 96px; height: 96px;
    border: 4px solid var(--silver); border-radius: 50%;
  }
  .brand-name { color: var(--gold); font-weight: 600; font-size: 30px; letter-spacing: 0.5px; }
</style>
</head>
<body>
  <main class="stage">
    <section class="card card--info" aria-label="Business card contact side">
      <div class="brand-mark"><span class="brand-mark__name">Pardeo</span></div>
      <div class="divider"></div>
      <div class="details">
        <p class="details__name">Harlan Webb</p>
        <p class="details__role">Founder, Managing Director</p>
        <p class="details__address">27 Corwen Street, Meridale Tower, #14-05 Singapore 058214</p>
        <ul class="contact-list">
          <li>
            <svg viewBox="0 0 24 24" aria-hidden="true"><path class="icon-fill" d="M6.6 10.8a15.1 15.1 0 0 0 6.6 6.6l2.2-2.2a1 1 0 0 1 1-.25 11.4 11.4 0 0 0 3.6.57 1 1 0 0 1 1 1V20a1 1 0 0 1-1 1A17 17 0 0 1 3 4a1 1 0 0 1 1-1h3.5a1 1 0 0 1 1 1c0 1.25.2 2.45.57 3.57a1 1 0 0 1-.25 1z"/></svg>
            +65 90481736
          </li>
          <li>
            <svg viewBox="0 0 24 24" aria-hidden="true"><rect class="icon-fill" x="2" y="5" width="20" height="14" rx="1"/><path class="icon-line" d="M3 6l9 7 9-7"/></svg>
            harlan.w@pardeotech.com
          </li>
        </ul>
      </div>
      <p class="registration">Company Registration no. <span class="registration__number">208716392K</span></p>
    </section>

    <section class="card card--brand" aria-label="Business card brand side">
      <div class="brand-circle"></div>
      <p class="brand-name">Pardeo Technologies</p>
    </section>
  </main>
</body>
</html>
```